Personal Brand (Influencer) Website

I'm looking for a brand new website design for a youtuber/influencer Dane Whitaker.

I'm looking for a sleek design that is visually appealing while still maintaining full functionality and user experience.

Here is our current website: http://danewhitakerhq.example/

I want to combine some of the best elements and designs from the following websites.

https://www.milofenwright.example/
https://www.renzovale.example/
https://quinnbarlow.example/
https://www.silasmerrow.example/
http://danewhitakerhq.example/
http://www.kenfrayle.example/

Here are the different tabs that I would need designed as well as the main page:

Home Page (main page)
Blogs
My story (about me)
Top 100 book list
Contact

Here are several links and social media handles for you to get a better gauge on the branding of Dane Whitaker:
https://www.videohub.example/channel/XQpar3k9v-T2mhZZ_QWrta7z
https://trend-rocket.example/market-blog/uncategorized/dane-whitaker-entrepreneur-winning-market-follow-data-ep-17/
https://danelisten2.pagepath.example/optin-48203917
https://www.snapgrid.example/officialdanewhitaker/

```html
<!DOCTYPE html>
<html lang="en">
<head>
<meta charset="utf-8">
<title>Dane Whitaker — Live Life On Your Terms</title>
<link href="https://fonts.googleapis.com/css2?family=Montserrat:wght@600;700;800&family=Open+Sans:wght@400;600;700;800&display=swap" rel="stylesheet">
<style>
:root{
  --blue:#0a84d8;
  --black:#000;
  --ink:#111;
  --white:#fff;
  --dark:#05070b;
  --muted:#cfd3d8;
}
*{box-sizing:border-box;margin:0;padding:0}
html,body{width:1200px;height:2799px;overflow:hidden;background:var(--black)}
body{position:relative;font-family:"Open Sans",Arial,sans-serif;color:var(--white)}
.abs{position:absolute}

/* header / hero */
.hero{left:0;top:0;width:1200px;height:615px;background:linear-gradient(100deg,#2c3238 0%,#6d7780 30%,#b9c6cf 45%,#5b6a78 65%,#30506e 100%)}
.hero-portrait{left:640px;top:40px;width:560px;height:575px;background:radial-gradient(ellipse at 55% 60%,#2a6cb0 0%,#22507e 45%,rgba(30,50,70,0) 75%)}
.brand{display:flex;align-items:center;gap:8px;font-family:"Montserrat",sans-serif;font-weight:700;color:var(--white);letter-spacing:1px}
.brand-square{width:16px;height:16px;border:2px solid var(--white)}
.site-brand{left:168px;top:32px;font-size:19px}
.nav{right:92px;top:36px;display:flex;gap:28px;font-size:11px;font-weight:600;letter-spacing:.3px}
.nav a{color:var(--white);text-decoration:none}
.nav a.active{color:var(--blue)}
.hero-title{left:150px;top:215px;width:520px;text-align:center;font-family:"Montserrat",sans-serif;font-weight:800;line-height:.95}
.hero-title .first{font-size:92px;color:var(--white);display:block}
.hero-title .last{font-size:74px;color:var(--blue);display:block}
.hero-tag{left:150px;top:418px;width:520px;text-align:center;font-family:"Montserrat",sans-serif;font-size:24px;font-weight:600;letter-spacing:1px}

/* meet */
.meet{left:0;top:615px;width:1200px;height:680px;background:linear-gradient(90deg,#3a3a3a 0%,#8f8f8f 25%,#6c6c6c 55%,#9a9a9a 80%,#5d5d5d 100%)}
.meet-portrait{left:0;top:615px;width:480px;height:665px;background:radial-gradient(ellipse at 40% 45%,#d8d8d8 0%,#6b6b6b 45%,rgba(60,60,60,0) 80%)}
.meet-copy{left:470px;top:736px;width:560px;text-align:center;font-family:"Montserrat",sans-serif;font-weight:800}
.meet-copy .kicker{font-size:28px;letter-spacing:1px;line-height:1.2}
.meet-copy .first{font-size:60px;line-height:1}
.meet-copy .last{font-size:46px;color:var(--ink);line-height:1.05}
.meet-role{font-family:"Open Sans",sans-serif;font-size:11px;font-weight:700;color:var(--ink);margin-top:10px;letter-spacing:.5px}
.meet-bio{left:490px;top:930px;width:520px;text-align:center;font-size:18px;line-height:1.5}
.meet-bio p+p{margin-top:22px}

/* signup band */
.band-shape{left:0;top:1220px}
.band-title{left:0;top:1302px;width:1200px;text-align:center;font-size:28px;font-weight:700;letter-spacing:1.5px}
.band-sub{left:0;top:1345px;width:1200px;text-align:center;font-size:10px;font-weight:700;letter-spacing:.5px}
.btn{display:flex;align-items:center;justify-content:center;font-size:11px;font-weight:700;letter-spacing:1px;color:var(--white);text-transform:uppercase}
.btn-signup{left:545px;top:1383px;width:110px;height:41px;background:var(--black)}

/* courses */
.course-offset{left:176px;top:1504px;width:298px;height:338px;background:var(--blue);transform:rotate(-3deg)}
.course-photo{left:163px;top:1512px;width:298px;height:335px;background:linear-gradient(160deg,#5b1fa0 0%,#a23ec9 45%,#2f0f55 100%);border:4px solid var(--white);transform:rotate(-2deg)}
.courses-copy{left:518px;top:1490px;width:560px;color:var(--ink)}
.courses-copy .kicker{font-size:36px;font-weight:800;letter-spacing:2px;line-height:1}
.courses-copy .kicker .hl{color:var(--blue)}
.courses-copy .title{font-family:"Montserrat",sans-serif;font-size:62px;font-weight:700;color:var(--blue);letter-spacing:2px;line-height:1.05}
.courses-copy .tagline{font-size:10px;font-weight:800;letter-spacing:.5px;margin-top:6px}
.courses-copy h3{font-size:20px;font-weight:800;margin-top:22px;letter-spacing:.3px}
.courses-copy .lead{font-size:19px;margin-top:2px}
.courses-copy .body{font-size:13px;line-height:1.4;width:460px;margin-top:16px}
.btn-course{left:520px;top:1822px;width:135px;height:37px;background:var(--blue)}

/* posts */
.posts-title{left:0;top:1935px;width:1200px;text-align:center;font-family:"Montserrat",sans-serif;font-size:46px;font-weight:800;letter-spacing:1px}
.posts-title .light{font-weight:700}
.posts-sub{left:0;top:1998px;width:1200px;text-align:center;font-size:11px;font-weight:700;letter-spacing:.5px}
.post{top:2054px;height:234px;display:flex;flex-direction:column;align-items:center;justify-content:flex-start;padding-top:68px}
.post-one{left:0;width:400px;background:linear-gradient(135deg,#1a1d22,#3b3f48 50%,#121418)}
.post-two{left:400px;width:412px;background:radial-gradient(ellipse at 50% 35%,#4f6fa8 0%,#1c2b52 45%,#070b18 100%)}
.post-three{left:812px;width:388px;background:linear-gradient(135deg,#6d5a3b,#a8946d 45%,#4d3f2a)}
.play{width:80px;height:80px}
.post-label{font-size:17px;font-weight:600;margin-top:22px;letter-spacing:.3px;text-shadow:0 1px 2px rgba(0,0,0,.6)}

/* footer */
.footer-brand{left:165px;top:2388px;font-size:22px}
.member{left:168px;top:2462px;font-size:11px;line-height:2.1}
.fcol{top:2380px;font-size:11px;line-height:2.2}
.fcol h4{font-size:16px;font-weight:600;margin-bottom:8px;line-height:1.2}
.fcol-about{left:452px}
.fcol-contact{left:612px}
.fcol-contact .gap{margin-top:12px}
.news{left:790px;top:2374px;width:290px;font-size:12px;line-height:1.3;color:var(--muted)}
.news-input{left:790px;top:2428px;width:275px;height:38px;background:#1b1d20;font-size:11px;padding:13px 0 0 18px;color:var(--white)}
.btn-submit{left:790px;top:2482px;width:140px;height:36px;background:var(--blue);font-size:15px;text-transform:none;letter-spacing:.5px}
.legal{left:170px;top:2652px;font-size:11px;line-height:2.3}
.social-title{left:880px;top:2620px;font-size:14px;font-weight:700}
.social{left:812px;top:2660px;display:flex;gap:12px}
.social-item{display:flex;align-items:center;gap:5px;font-size:11px}
.social-dot{width:26px;height:26px;border:2px solid var(--white);border-radius:50%}
.social-item.first .social-dot{border-color:var(--blue)}
</style>
</head>
<body>

<header>
  <div class="abs hero" role="img" aria-label="Photo of a glacier and mountains with cloudy sky"></div>
  <div class="abs hero-portrait" role="img" aria-label="Portrait of Dane Whitaker in a beanie and blue jacket"></div>
  <div class="abs brand site-brand"><span class="brand-square"></span>DANE WHITAKER</div>
  <nav class="abs nav">
    <a class="active" href="#">HOME</a><a href="#">BLOGS</a><a href="#">MY STORY</a><a href="#">TOP BOOKS</a><a href="#">CONTACT</a>
  </nav>
  <h1 class="abs hero-title"><span class="first">DANE</span><span class="last">WHITAKER</span></h1>
  <p class="abs hero-tag">LIVE LIFE ON YOUR TERMS</p>
</header>

<section>
  <div class="abs meet" role="img" aria-label="Black and white mountain valley landscape"></div>
  <div class="abs meet-portrait" role="img" aria-label="Black and white photo of Dane Whitaker smiling in a cap with a backpack"></div>
  <div class="abs meet-copy">
    <div class="kicker">MEET</div>
    <div class="first">DANE</div>
    <div class="last">WHITAKER</div>
    <div class="meet-role">ENTREPRENEUR AUHOR SPEAKER</div>
  </div>
  <div class="abs meet-bio">
    <p>Dane Whitaker is a 7 figure Ecommerce Entrepreneur, Speaker, Inventor, Bio-hacker, and Positive thinker. He believes the world is getting better every day.</p>
    <p>Dane went from 0 to 6 Million in 6 Months selling Solar Shades on Marketly Direct. He also proposed to his wife in Outer Space. He is not your typical person</p>
  </div>
</section>

<section>
  <svg class="abs band-shape" width="1200" height="187" viewBox="0 0 1200 187">
    <polygon points="0,60 1200,0 1200,187 0,187" fill="var(--blue)"/>
  </svg>
  <h2 class="abs band-title">JOIN 40,000+ MARKETLY SELLERS.</h2>
  <p class="abs band-sub">SIGN UP FOR THE LATEST VIDEOS &amp; FREE CONTENT.</p>
  <a class="abs btn btn-signup">SIGNUP</a>
</section>

<section>
  <svg class="abs" style="left:0;top:1407px" width="1200" height="520" viewBox="0 0 1200 520">
    <polygon points="0,0 1200,0 1200,446 0,506" fill="var(--white)"/>
  </svg>
  <div class="abs course-offset"></div>
  <div class="abs course-photo" role="img" aria-label="Photo of a man with glowing neon face paint"></div>
  <div class="abs courses-copy">
    <div class="kicker">FEAT<span class="hl">U</span>RED</div>
    <div class="title">COURSES</div>
    <div class="tagline">OPPORTUNITIES DON'T HAPPEN. YOU CREATE THEM.</div>
    <h3>THE FIRST FREE MARKETLY PRIVATE LABEL COURSE</h3>
    <p class="lead">I am giving away everything that I know for free.</p>
    <p class="body">Myself &amp; the top Marketly sellers will be teaching you everything that you need to know about creating &amp; managing a thriving Marketly Direct Business so that you can live your life on your terms.</p>
  </div>
  <a class="abs btn btn-course">SIGNUP HERE</a>
</section>

<section>
  <h2 class="abs posts-title"><span class="light">RECENT</span> POSTS</h2>
  <p class="abs posts-sub">KEEP GOING. START CHASING THE PASSION.</p>
  <article class="abs post post-one" role="img" aria-label="Video still of a speaker on stage">
    <svg class="play" viewBox="0 0 82 82"><circle cx="41" cy="41" r="39" fill="none" stroke="#fff" stroke-width="2"/><polygon points="34,27 58,41 34,55" fill="none" stroke="#fff" stroke-width="2"/></svg>
    <span class="post-label">STAGE TALK</span>
  </article>
  <article class="abs post post-two" role="img" aria-label="Video still of a speaker with arms raised before a crowd">
    <svg class="play" viewBox="0 0 82 82"><circle cx="41" cy="41" r="39" fill="none" stroke="#fff" stroke-width="2"/><polygon points="34,27 58,41 34,55" fill="none" stroke="#fff" stroke-width="2"/></svg>
    <span class="post-label">NOT YOUR MENTOR</span>
  </article>
  <article class="abs post post-three" role="img" aria-label="Video still of two people talking outdoors">
    <svg class="play" viewBox="0 0 82 82"><circle cx="41" cy="41" r="39" fill="none" stroke="#fff" stroke-width="2"/><polygon points="34,27 58,41 34,55" fill="none" stroke="#fff" stroke-width="2"/></svg>
    <span class="post-label">DEEP ROOTS SUNDAY</span>
  </article>
</section>

<footer>
  <div class="abs brand footer-brand"><span class="brand-square"></span>DANE WHITAKER</div>
  <div class="abs member">
    <p>Member:&nbsp; Lakeside Producers Guild</p>
    <p>Plains Society of Film Crafts</p>
  </div>
  <div class="abs fcol fcol-about">
    <h4>About</h4>
    <p>About Us</p><p>Jobs</p><p>Hollow Brook Foundation</p><p>Pricing</p>
  </div>
  <div class="abs fcol fcol-contact">
    <h4>CONTACT US</h4>
    <p>418 Harlow Rd.</p><p>Brenton, ST 55102</p>
    <p class="gap">0000 00000 0000</p><p>contact@mailbox.example</p>
  </div>
  <p class="abs news">Receive valuable insights and helpful articles about the latest trends in immersive marketing.</p>
  <div class="abs news-input">Email</div>
  <a class="abs btn btn-submit">Submit</a>
  <div class="abs legal">
    <p>© copyright 2018 website. All rights reserved.</p>
    <p>Privacy &amp; terms</p>
  </div>
  <p class="abs social-title">Join us on</p>
  <div class="abs social">
    <span class="social-item first"><span class="social-dot"></span>Chirpline</span>
    <span class="social-item"><span class="social-dot"></span>Circlebook</span>
    <span class="social-item"><span class="social-dot"></span>Loopnest</span>
    <span class="social-item"><span class="social-dot"></span>videohub</span>
  </div>
</footer>

</body>
</html>
```